Individual Needs Design for Marketing Package

****IMPORTANT: Note that I have arranged an agreement with a specific designer to complete the design for the portfolio. Please do not submit any designs***

Goal
I recently resigned from my job in Canada, and I am moving down to Silicon Valley to pursue a career in the technology startup scene - initially doing technical sales. So my goal is to get a sales position with a startup tech company.

In order to land a sales position, I will be going to a startup conference in Silicon Valley which brings together over 2,000 startup technology companies. My goal is to meet the owners of some of these companies and demonstrate that I can be a valuable asset to their company. My challenge is that I have no existing relationships in Silicon Valley and limited experience in sales. So I have put together a portfolio of some of my most significant accomplishments over the past 6 years (see attached file). My hope is that this portfolio will convey that even though I have limited experience, I am passionate, driven, and loyal with a proven track record of achievement. After talking with them for 30 minutes and developing a rapport, I plan on giving this accomplishment portfolio (in addition to my resume) to CEOs of companies for which I could potentially work.

Message to Communicate
After someone reads my portfolio, I want them to view me as passionate, driven, and loyal with a proven track record of achievement. The design can communicate this message in a subtle way. The portfolio should also speak to my professionalism. It should certainly have some personality, but it should err on the side of professionalism.

Competitors
My competitors will be other people at the conference also looking to get sales positions with these startup companies. My main points of differentiation are that I am passionate, driven, and loyal with a proven track record of results. I would like this to be made a feature of the design.

Design Templates
I do not have any specific fonts or colours that I need you to use. The colours scheme and fonts selected should reinforce my key message.

Other Information
I do not own any specialized design software - only the basic microsoft word and powerpoint. However, I will need to be able to add new accomplishments to the portfolio and edit existing ones. Please let me know how this will be possible. I am not sure if it is possible to convert the final file into a file format that I can edit.

Notice that I have arranged the pages into sections. Feel free to rearrange the content within the sections, but please do not change the order of the sections

The size for the marketing package will be regular 8.5 x 11".
Updates

Target Market(s)

The people that will be reading my portfolio are owners of small technology companies in Silicon Valley. They are typically 28-35 years old, and highly logical thinkers. This means that the content is what is ultimately going to sell myself, but the design is what will make them want to read it. Therefore, the content should really stand out over the design.

Industry/Entity Type

Marketing

Requirements
Must have
• ****IMPORTANT: Note that I have arranged an agreement with a specific designer to complete the design for the portfolio. Please do not submit any designs***

I really view this portfolio as my personal marketing package, and that is where I need your expertise. I need you to take the content that I have in my portfolio and turn it into a personal marketing package. I need you to:

1. Design the cover page
2. Design the template for the content pages
3. Format the pictures and text to best fit the design of the pages**

** I would like the final design submission to include the pictures and text included in the attached file all fully formatted. However, when submitting the first iterations, please do not feel obligated to format the entire portfolio because I know that it can be time consuming. Just formatting the title page and the first content page should be enough to give me an idea of what the final portfolio will look like. Once we narrow it down to the final few designs, then we can start formatting the complete portfolio.

```html
<!DOCTYPE html>
<html lang="en">
<head>
<meta charset="utf-8">
<title>Daniel Harper – Sales Spread</title>
<link href="https://fonts.googleapis.com/css2?family=Lato:wght@300;400;700;900&display=swap" rel="stylesheet">
<style>
  :root {
    --backdrop: #454341;
    --paper: #ffffff;
    --ink: #2e2e2e;
    --accent: #3a87cc;
    --accent-dark: #0b5a8a;
    --zero: #555555;
  }
  html, body {
    margin: 0;
    padding: 0;
    width: 1200px;
    height: 900px;
    overflow: hidden;
    background: var(--backdrop);
    font-family: "Lato", Arial, sans-serif;
  }
  .canvas { position: relative; width: 1200px; height: 900px; }
  .spread {
    position: absolute;
    left: 72px; top: 246px;
    width: 1056px; height: 409px;
    background: var(--paper);
  }
  .story {
    position: absolute;
    text-align: right;
    color: var(--ink);
  }
  .story--2011 { right: 565px; top: 52px; }
  .story--2012 { right: 28px; top: 52px; }
  .story__title {
    margin: 0 0 4px;
    font-size: 14.5px;
    font-weight: 700;
    color: var(--accent);
  }
  .story__body {
    margin: 0;
    font-size: 15.5px;
    font-weight: 300;
    line-height: 22px;
  }
  .chart { position: absolute; left: 0; top: 0; overflow: visible; }
  .chart .bar { fill: var(--accent); }
  .chart .bar--lead { fill: var(--accent-dark); }
  .chart .value { fill: #fff; font: 900 8.5px "Lato", sans-serif; }
  .chart .zero { fill: var(--zero); font: 400 10px "Lato", sans-serif; }
  .chart .who { fill: var(--ink); font: 700 4.5px "Lato", sans-serif; }
  .folio {
    position: absolute;
    top: 394px;
    font-size: 6px;
    letter-spacing: 0.3px;
    color: var(--ink);
    text-transform: uppercase;
    display: flex; align-items: center; gap: 6px;
  }
  .folio--left { left: 29px; }
  .folio--right { right: 29px; }
  .folio .section { color: var(--accent); }
  .folio__mark { width: 16px; height: 16px; background: var(--ink); }
</style>
</head>
<body>
<div class="canvas">
  <section class="spread">
    <article class="story story--2011">
      <h2 class="story__title">Summer of 2011 (May 1-Aug 31)</h2>
      <p class="story__body">I had no sales experience or formal training, but as a<br>result of my drive and commitment, I attended more sales<br>calls and raised more internships than any of the other 18<br>business development coordinators across Canada.</p>
    </article>
    <article class="story story--2012">
      <h2 class="story__title">Summer of 2012 (May 1-Aug 31)</h2>
      <p class="story__body">In summer of 2012, I took on the role again with a focus on<br>working smarter – not harder. As a result, I increased the number<br>of internships I raised by 25% over the previous summer while<br>attending fewer marketing calls. I was again the top business<br>development representative in the country.</p>
    </article>

    <!-- 2011 chart: baseline 309, unit 19.2, pitch 17.8 -->
    <svg class="chart" width="1056" height="409" viewBox="0 0 1056 409" aria-label="Internships raised per coordinator, summer 2011">
      <g>
        <rect class="bar bar--lead" x="176.6" y="193.8" width="15.4" height="115.2"/><text class="value" x="179.6" y="203.8">6</text>
        <rect class="bar" x="194.4" y="251.4" width="15.4" height="57.6"/><text class="value" x="199.6" y="261.4">3</text>
        <rect class="bar" x="212.2" y="251.4" width="15.4" height="57.6"/><text class="value" x="217.4" y="261.4">3</text>
        <rect class="bar" x="230" y="270.6" width="15.4" height="38.4"/><text class="value" x="235.2" y="280.6">2</text>
        <rect class="bar" x="247.8" y="270.6" width="15.4" height="38.4"/><text class="value" x="253" y="280.6">2</text>
        <rect class="bar" x="265.6" y="270.6" width="15.4" height="38.4"/><text class="value" x="270.8" y="280.6">2</text>
        <rect class="bar" x="283.4" y="270.6" width="15.4" height="38.4"/><text class="value" x="288.6" y="280.6">2</text>
        <rect class="bar" x="301.2" y="289.8" width="15.4" height="19.2"/><text class="value" x="306.4" y="299.8">1</text>
        <rect class="bar" x="319" y="289.8" width="15.4" height="19.2"/><text class="value" x="324.2" y="299.8">1</text>
        <rect class="bar" x="336.8" y="289.8" width="15.4" height="19.2"/><text class="value" x="342" y="299.8">1</text>
        <rect class="bar" x="354.6" y="289.8" width="15.4" height="19.2"/><text class="value" x="359.8" y="299.8">1</text>
        <text class="zero" x="374" y="308">0</text><text class="zero" x="391.8" y="308">0</text><text class="zero" x="409.6" y="308">0</text><text class="zero" x="427.4" y="308">0</text><text class="zero" x="445.2" y="308">0</text><text class="zero" x="463" y="308">0</text><text class="zero" x="480.8" y="308">0</text>
      </g>
      <g>
        <text class="who" transform="translate(186,346) rotate(-90)">Dan Harper</text>
        <text class="who" transform="translate(204,326) rotate(-90)">Rep</text><text class="who" transform="translate(222,326) rotate(-90)">Rep</text><text class="who" transform="translate(240,326) rotate(-90)">Rep</text><text class="who" transform="translate(257,326) rotate(-90)">Rep</text><text class="who" transform="translate(275,326) rotate(-90)">Rep</text><text class="who" transform="translate(293,326) rotate(-90)">Rep</text><text class="who" transform="translate(311,326) rotate(-90)">Rep</text><text class="who" transform="translate(329,326) rotate(-90)">Rep</text><text class="who" transform="translate(346,326) rotate(-90)">Rep</text><text class="who" transform="translate(364,326) rotate(-90)">Rep</text><text class="who" transform="translate(382,326) rotate(-90)">Rep</text><text class="who" transform="translate(400,326) rotate(-90)">Rep</text><text class="who" transform="translate(418,326) rotate(-90)">Rep</text><text class="who" transform="translate(435,326) rotate(-90)">Rep</text><text class="who" transform="translate(453,326) rotate(-90)">Rep</text><text class="who" transform="translate(471,326) rotate(-90)">Rep</text><text class="who" transform="translate(489,326) rotate(-90)">Rep</text>
      </g>
    </svg>

    <!-- 2012 chart: baseline 309, unit 15, pitch 18.7 -->
    <svg class="chart" width="1056" height="409" viewBox="0 0 1056 409" aria-label="Internships raised per representative, summer 2012">
      <g>
        <rect class="bar bar--lead" x="693" y="189" width="16.3" height="120"/><text class="value" x="696" y="199">8</text>
        <rect class="bar" x="711.7" y="264" width="16.3" height="45"/><text class="value" x="717" y="274">3</text>
        <rect class="bar" x="730.4" y="264" width="16.3" height="45"/><text class="value" x="735.7" y="274">3</text>
        <rect class="bar" x="749.1" y="279" width="16.3" height="30"/><text class="value" x="754.4" y="289">2</text>
        <rect class="bar" x="767.8" y="279" width="16.3" height="30"/><text class="value" x="773.1" y="289">2</text>
        <rect class="bar" x="786.5" y="294" width="16.3" height="15"/><text class="value" x="791.8" y="304">1</text>
        <rect class="bar" x="805.2" y="294" width="16.3" height="15"/><text class="value" x="810.5" y="304">1</text>
        <rect class="bar" x="823.9" y="294" width="16.3" height="15"/><text class="value" x="829.2" y="304">1</text>
        <rect class="bar" x="842.6" y="294" width="16.3" height="15"/><text class="value" x="847.9" y="304">1</text>
        <rect class="bar" x="861.3" y="294" width="16.3" height="15"/><text class="value" x="866.6" y="304">1</text>
        <rect class="bar" x="880" y="294" width="16.3" height="15"/><text class="value" x="885.3" y="304">1</text>
        <text class="zero" x="900" y="308">0</text><text class="zero" x="918.7" y="308">0</text><text class="zero" x="937.4" y="308">0</text><text class="zero" x="956.1" y="308">0</text><text class="zero" x="974.8" y="308">0</text><text class="zero" x="993.5" y="308">0</text><text class="zero" x="1012.2" y="308">0</text>
      </g>
      <g>
        <text class="who" transform="translate(703,346) rotate(-90)">Dan Harper</text>
        <text class="who" transform="translate(722,326) rotate(-90)">Rep</text><text class="who" transform="translate(740,326) rotate(-90)">Rep</text><text class="who" transform="translate(759,326) rotate(-90)">Rep</text><text class="who" transform="translate(778,326) rotate(-90)">Rep</text><text class="who" transform="translate(796,326) rotate(-90)">Rep</text><text class="who" transform="translate(815,326) rotate(-90)">Rep</text><text class="who" transform="translate(834,326) rotate(-90)">Rep</text><text class="who" transform="translate(853,326) rotate(-90)">Rep</text><text class="who" transform="translate(871,326) rotate(-90)">Rep</text><text class="who" transform="translate(890,326) rotate(-90)">Rep</text><text class="who" transform="translate(909,326) rotate(-90)">Rep</text><text class="who" transform="translate(927,326) rotate(-90)">Rep</text><text class="who" transform="translate(946,326) rotate(-90)">Rep</text><text class="who" transform="translate(965,326) rotate(-90)">Rep</text><text class="who" transform="translate(984,326) rotate(-90)">Rep</text><text class="who" transform="translate(1002,326) rotate(-90)">Rep</text><text class="who" transform="translate(1021,326) rotate(-90)">Rep</text>
      </g>
    </svg>

    <footer class="folio folio--left">P. 10 | Daniel Harper | <span class="section">Sales</span></footer>
    <footer class="folio folio--right"><span class="folio__mark"></span>Daniel Harper | <span class="section">Sales</span> | P. 11</footer>
  </section>
</div>
</body>
</html>
```